New Corporate Email Signature with Custom GIF VAM Electric LLC & VAM Fire & Security

Project Overview
VAM Electric LLC and VAM Fire & Security are seeking a professional, polished, and technically robust corporate email signature design. The project has two integrated deliverables:
A custom animated GIF representing both sides of our business
A complete corporate email signature layout designed for real-world compatibility (Gmail, Outlook, iOS, Android)
Our brand aesthetic is corporate, conservative, and clean. We value clarity, trust, professionalism, and subtle creativity β€” nothing overly flashy or cartoonish.
This design will be used across the entire company and must be visually aligned with our brand while remaining technically dependable.

PART 1 β€” Animated GIF Requirements
The GIF will be the core visual anchor of the new signature.
It must be clean, smooth, subtle, and optimized for email use.
βš™ Technical Requirements
Max file size: 150–200 KB (smaller is better)
Dimensions: approx 300px width (flexible, but must look good small)
Looping: continuous loop
Style: professional, minimalistic transitions

No rapid flashing or harsh animations
Must export cleanly into a format email clients accept

🎞 GIF Animation Sequence
Phase 1 β€” VAM Electric (VE)
Use the yellow β€œVE” avatar logo (provided).
Animation flow:
VE avatar appears
Full name β€œVAM Electric LLC” slides in, fades in, or otherwise appears smoothly
A scrolling or cycling list of service offerings displays:
EV Charging Stations
Generator & Transformers
Testing & Troubleshooting
LED Lighting Upgrades
After the list is shown, the entire VE segment fades out

Phase 2 β€” VAM Fire & Security (VF)
Use the red β€œVF” avatar logo (provided).
Animation flow mirrors Phase 1:
VF avatar appears
Full name β€œVAM Fire & Security” slides/fades in
Scrolling or cycling list of services displays:
Fire Alarm Upgrades
KDLT 58 Test & Inspect
Security Surveillance Systems
Access Control Systems
Data & Fiber Optic Cabling
Fade out β†’ loop back to VE
Creative Direction

Designers are encouraged to use:
Clean transitions
Soft fades
Professional typography
Modern minimalism
Consistent brand colors
High clarity at small sizes

Avoid:
Busy motion
Hard flashes
Excessive text overlays
Overly long transitions

The goal: a smooth, corporate-grade rotation that fits seamlessly into an email signature.

PART 2 β€” Corporate Email Signature Design

The signature must be visually appealing, brand-aligned, and structurally bulletproof across all major email systems.
πŸ“ Required Elements
πŸ‘€ Left Side Content
Circular headshot (we will supply final photos)
Social media icons with embedded URLs:
Social link 1
Social link 2
Social link 4 Business Profile
Social link 3

Icons should be clean, modern, and in alignment with brand colors
πŸ“„ Right Side Content
Name
Title
VAM Electric LLC / VAM Fire & Security (depending on user)
Phone number
Email address
License# 42860
Physical office address: 348 Brambleton Ave, Ferncliff NJ 07391

Small CTA for newsletter signup (button or micro-banner)

🏒 Branding Assets Provided

You will receive:
VE avatar logo
VF avatar logo
Full-name VE logo
Full-name VF logo

These should be incorporated naturally and professionally.

Design Requirements

Conservative corporate styling

Clean typography

Balanced use of white space

Professional hierarchy

Light and dark mode compatibility preferred

Layout should not rely on one large image

All images should export cleanly for hosting on servers/CDN

Avoid overly tall signatures

The final signature must present as modern, trustworthy, and technically reliable across platforms.

πŸ§ͺ Compatibility Requirements

The signature must display correctly in:

Gmail (web and mobile)

Outlook (desktop & online)

Apple Mail

iPhone Mail

Android mail apps

Designers must avoid DIV-based layouts and instead propose a layout that can be implemented using table-based HTML, which is the industry standard for email compatibility.

You do not need to build the HTML β€” only supply the final layered design (PSD/AI/Figma) plus a clear structural layout that can be converted to HTML later.

πŸ“¦ Deliverables
1. Animated GIF

Final optimized GIF

Source file (After Effects, Photoshop, or equivalent)

Export guidelines so we can reproduce future versions

2. Email Signature Design

Full static design mockup

Modular layout for each employee

Icon set for social media

Newsletter CTA element

Clear spacing, alignment, and typography specifications

All source files (PSD, AI, Figma, etc.)

🧭 Creative Guidance Summary

We want:
βœ” Modern
βœ” Corporate
βœ” Minimalistic
βœ” Professional
βœ” Clean motion
βœ” Consistent branding
βœ” Email-safe elements

We do not want:
✘ Flashy marketing look
✘ Overly colorful or playful styles
✘ Hard-to-read fonts
✘ Heavy animation
✘ Oversized signatures

πŸ›  Tools & Format Flexibility

We allow full creative freedom regarding:

Animation style

Typography choices

Structuring of the two-column layout

How the service lists scroll or cycle

As long as the end result is clean, brand-aligned, professional, and email-compatible.

πŸ’¬ Final Note to Designers

We encourage creativity within the boundaries of corporate professionalism.
This signature will represent our company every time an email is sent β€” it must communicate trust, clarity, expertise, and brand strength.

```html
<!DOCTYPE html>
<html lang="en">
<head>
<meta charset="utf-8">
<title>VAM Email Signatures</title>
<link rel="stylesheet" href="https://fonts.googleapis.com/css2?family=Roboto:wght@500;700&display=swap">
<style>
:root{
  --stage:#a2a2a2;
  --panel-grey:#7b7b7b;
  --band-grey:#7b7b7b;
  --fire-red:#e8232f;
  --electric-yellow:#e8cf14;
  --ink:#262626;
  --ink-soft:#333333;
  --white:#ffffff;
  --logo-grey:#585858;
  --icon-border:#777777;
}
*{box-sizing:border-box;margin:0;padding:0}
html,body{width:1189px;height:1200px;overflow:hidden;background:var(--stage)}
body{font-family:"Roboto",Arial,sans-serif}
.stage{width:1088px;height:1098px;transform:scale(1.0929);transform-origin:0 0;position:relative}
.signature{position:absolute;left:144px;width:800px;height:400px;overflow:hidden;box-shadow:0 20px 50px rgba(0,0,0,.25)}
.signature--fire{top:124px;background:var(--white)}
.signature--electric{top:574px;background:var(--band-grey)}
.shapes{position:absolute;inset:0}
.headshot{position:absolute;background:linear-gradient(180deg,#d9d9d9 0%,#c4c4c4 60%,#5d5f66 100%)}
.signature--fire .headshot{left:50px;top:79px;width:196px;height:195px;border-radius:50px}
.signature--electric .headshot{left:44px;top:37px;width:218px;height:218px;border-radius:56px}
.socials{position:absolute;display:flex;gap:11px}
.social{width:48px;height:48px;border-radius:50%;background:var(--white);display:block}
.signature--fire .socials{left:36px;top:300px}
.signature--electric .socials{left:41px;top:290px}
.person{position:absolute;font-weight:700;white-space:nowrap}
.person__name{font-size:30px;line-height:1;letter-spacing:.2px}
.person__title{font-size:17px;margin-top:14px}
.signature--fire .person{left:312px;top:28px;color:var(--white)}
.signature--electric .person{left:339px;top:38px;color:var(--ink-soft)}
.brand{position:absolute;font-weight:700;font-size:17px;letter-spacing:1.4px;white-space:nowrap;text-transform:uppercase}
.signature--fire .brand{left:534px;top:82px;color:var(--fire-red)}
.signature--electric .brand{left:554px;top:70px;color:var(--logo-grey)}
.brand__mark{display:inline-block;width:12px;height:12px;margin-right:8px;vertical-align:0}
.signature--fire .brand__mark{background:var(--fire-red)}
.signature--electric .brand__mark{background:var(--electric-yellow)}
.contacts{position:absolute;list-style:none}
.contact{display:flex;align-items:center;font-size:19px;font-weight:700;color:var(--ink);line-height:1.35}
.contact svg{flex:none;width:42px;height:42px}
.signature--fire .contacts{left:352px;top:159px}
.signature--fire .contact{gap:19px;margin-bottom:17px}
.signature--electric .contacts{left:342px;top:143px}
.signature--electric .contact{gap:21px;margin-bottom:17px}
.signature--electric .contact svg{width:46px;height:46px}
.newsletter{position:absolute;left:330px;top:360px;display:flex;align-items:center;gap:26px}
.signature--electric .newsletter{top:361px}
.newsletter__text{color:var(--white);font-size:19px;font-weight:700}
.newsletter__button{background:var(--white);border-radius:14px;width:92px;height:28px;display:flex;align-items:center;justify-content:center;font-size:15px;font-weight:700}
.signature--fire .newsletter__button{color:var(--fire-red)}
.signature--electric .newsletter__button{color:var(--band-grey)}
</style>
</head>
<body>
<main class="stage">

  <section class="signature signature--fire" aria-label="VAM Fire &amp; Security email signature">
    <svg class="shapes" width="800" height="400" viewBox="0 0 800 400" aria-hidden="true">
      <rect x="0" y="0" width="306" height="400" fill="var(--panel-grey)"/>
      <path d="M236,0 H800 V130 H310 Q236,130 236,56 Z" fill="var(--fire-red)"/>
      <path d="M244,0 V60 Q244,118 300,124" fill="none" stroke="var(--white)" stroke-width="4"/>
      <path d="M256,0 V58 Q256,110 304,118" fill="none" stroke="var(--white)" stroke-width="4"/>
      <path d="M268,0 V56 Q268,100 310,110" fill="none" stroke="var(--white)" stroke-width="4"/>
      <path d="M498,0 H800 V124 H556 Q498,124 498,66 Z" fill="var(--white)"/>
      <path d="M278,400 V398 Q278,348 328,348 H800 V400 Z" fill="var(--fire-red)"/>
    </svg>
    <div class="headshot" role="img" aria-label="Headshot of the team member"></div>
    <nav class="socials" aria-label="Social profiles">
      <a class="social" aria-label="Social profile 1"></a>
      <a class="social" aria-label="Social profile 2"></a>
      <a class="social" aria-label="Social profile 3"></a>
      <a class="social" aria-label="Social profile 4"></a>
    </nav>
    <div class="person">
      <p class="person__name">MARK LEE</p>
      <p class="person__title">Chief Manager</p>
    </div>
    <p class="brand"><span class="brand__mark"></span>VAM Fire &amp; Security</p>
    <ul class="contacts">
      <li class="contact">
        <svg viewBox="0 0 42 42" aria-hidden="true"><circle cx="21" cy="21" r="19.5" fill="var(--white)" stroke="var(--icon-border)" stroke-width="2.5"/><path d="M15.5,13 l3,0 1.5,4 -2,1.5 q1.5,3.5 5,5 l1.5,-2 4,1.5 0,3 q-1,2 -3,2 q-10,-1 -12,-12 q0,-2 2,-3z" fill="var(--fire-red)"/></svg>
        <span>+1 555 214 3087</span>
      </li>
      <li class="contact">
        <svg viewBox="0 0 42 42" aria-hidden="true"><circle cx="21" cy="21" r="21" fill="var(--icon-border)"/><rect x="13" y="15" width="16" height="12" rx="1.5" fill="var(--white)"/><path d="M13.5,16 L21,22 L28.5,16" fill="none" stroke="var(--icon-border)" stroke-width="1.5"/></svg>
        <span>info@vamsample.com</span>
      </li>
      <li class="contact">
        <svg viewBox="0 0 42 42" aria-hidden="true"><circle cx="21" cy="21" r="19.5" fill="var(--white)" stroke="var(--icon-border)" stroke-width="2.5"/><path d="M21,30 q-7,-7.5 -7,-12 a7,7 0 0 1 14,0 q0,4.5 -7,12z" fill="var(--fire-red)"/><circle cx="21" cy="18" r="2.6" fill="var(--white)"/></svg>
        <span>348 Brambleton Ave, Ferncliff NJ 07391<br>License# 42860</span>
      </li>
    </ul>
    <div class="newsletter">
      <span class="newsletter__text">Sign Up for the New Updates</span>
      <span class="newsletter__button">SIGN UP</span>
    </div>
  </section>

  <section class="signature signature--electric" aria-label="VAM Electric LLC email signature">
    <svg class="shapes" width="800" height="400" viewBox="0 0 800 400" aria-hidden="true">
      <path d="M256,0 H800 V348 H346 Q296,348 296,298 V40 Q296,0 256,0 Z" fill="var(--electric-yellow)"/>
      <path d="M488,0 H498 L538,110 H528 Z" fill="var(--logo-grey)"/>
      <path d="M498,0 H800 V110 H538 Z" fill="var(--white)"/>
    </svg>
    <div class="headshot" role="img" aria-label="Headshot of the team member"></div>
    <nav class="socials" aria-label="Social profiles">
      <a class="social" aria-label="Social profile 1"></a>
      <a class="social" aria-label="Social profile 2"></a>
      <a class="social" aria-label="Social profile 3"></a>
      <a class="social" aria-label="Social profile 4"></a>
    </nav>
    <div class="person">
      <p class="person__name">MARK LEE</p>
      <p class="person__title">Chief Manager</p>
    </div>
    <p class="brand"><span class="brand__mark"></span>VAM Electric LLC</p>
    <ul class="contacts">
      <li class="contact">
        <svg viewBox="0 0 46 46" aria-hidden="true"><rect x="1.5" y="1.5" width="43" height="43" rx="14" fill="var(--white)" stroke="var(--icon-border)" stroke-width="2.5"/><path d="M17.5,15 l3,0 1.5,4 -2,1.5 q1.5,3.5 5,5 l1.5,-2 4,1.5 0,3 q-1,2 -3,2 q-10,-1 -12,-12 q0,-2 2,-3z" fill="var(--electric-yellow)"/></svg>
        <span>+1 555 214 3087</span>
      </li>
      <li class="contact">
        <svg viewBox="0 0 46 46" aria-hidden="true"><rect x="0" y="0" width="46" height="46" rx="15" fill="var(--icon-border)"/><rect x="15" y="17" width="16" height="12" rx="1.5" fill="var(--white)"/><path d="M15.5,18 L23,24 L30.5,18" fill="none" stroke="var(--icon-border)" stroke-width="1.5"/></svg>
        <span>info@vamsample.com</span>
      </li>
      <li class="contact">
        <svg viewBox="0 0 46 46" aria-hidden="true"><rect x="1.5" y="1.5" width="43" height="43" rx="14" fill="var(--white)" stroke="var(--icon-border)" stroke-width="2.5"/><path d="M23,32 q-7,-7.5 -7,-12 a7,7 0 0 1 14,0 q0,4.5 -7,12z" fill="var(--electric-yellow)"/><circle cx="23" cy="20" r="2.6" fill="var(--white)"/></svg>
        <span>348 Brambleton Ave, Ferncliff NJ 07391<br>License# 42860</span>
      </li>
    </ul>
    <div class="newsletter">
      <span class="newsletter__text">Sign Up for the New Updates</span>
      <span class="newsletter__button">SIGN UP</span>
    </div>
  </section>

</main>
</body>
</html>
```